Our new beauty salon requires a price list brochure

Our beauty clinic is a medical grade skin care clinic. So our salon is very clinical and professional in appearance. I would like the colours to be similar to our logo design with some nice texture or abstract shapes thrown in.
Pricelist, contact details and logo is attached
I would prefer it to be a 3 fold brochure.

Target Market(s)

Females aged 30-50

Colors
85acd3
cedeed
c4c4c4
5c5c5c
000000
ffffff
eea3c7
f9d9e8
dbdbdb

Requirements
Must have
• easy to read

```html
<!DOCTYPE html>
<html lang="en">
<head>
<meta charset="utf-8">
<title>Maren Aesthetics – Price List</title>
<link href="https://fonts.googleapis.com/css2?family=Figtree:wght@400;600;700&display=swap" rel="stylesheet">
<style>
  :root {
    --panel: #e5e1e2;
    --paper: #ffffff;
    --accent: #85acd3;
    --ink: #3f4246;
    --brand: #4f5d6b;
    --row: 21.35px;
  }
  * { margin: 0; padding: 0; box-sizing: border-box; }
  html, body { width: 1200px; height: 848px; overflow: hidden; background: var(--paper); }
  body { font-family: "Figtree", sans-serif; color: var(--ink); }
  .sheet { position: relative; width: 1200px; height: 848px; background: var(--paper); }
  .brand-panel { position: absolute; left: 0; top: 0; width: 400px; height: 848px; background: var(--panel); }

  .brand { position: absolute; left: 0; width: 400px; top: 372px; text-align: center; color: var(--brand); font-weight: 400; }
  .brand-name { font-size: 58px; letter-spacing: 2px; line-height: 1; }
  .brand-sub { font-size: 12px; letter-spacing: 10px; margin-top: 28px; padding-left: 10px; margin-left: -120px; }

  .contact { position: absolute; left: 66px; top: 653px; color: var(--brand); font-size: 13.6px; font-weight: 600; line-height: 17px; }
  .contact .phone { margin-top: 4px; }
  .contact .online { margin-top: 21px; font-size: 12px; line-height: 15.6px; }

  .section-title { position: absolute; color: var(--accent); font-weight: 700; font-size: 16.5px; letter-spacing: 0.4px; text-align: center; width: 320px; }
  .price-list { position: absolute; list-style: none; font-size: 14px; letter-spacing: 0.3px; }
  .price-list li { display: flex; height: var(--row); line-height: var(--row); }
  .price-list li.gap { height: var(--row); }
  .price-list .item { flex: 1; white-space: nowrap; }

  .ipl-title { left: 440px; top: 64px; }
  .ipl { left: 463px; top: 104px; width: 270px; }
  .ipl .item { max-width: 234px; }

  .photo-title { left: 440px; top: 641px; }
  .photo { left: 458px; top: 683px; width: 275px; }

  .wax-title { left: 840px; top: 64px; }
  .wax { left: 863px; top: 104px; width: 262px; }

  .mens-title { left: 840px; top: 568px; }
  .mens { left: 863px; top: 609px; width: 262px; }
</style>
</head>
<body>
<main class="sheet">
  <aside class="brand-panel">
    <div class="brand">
      <div class="brand-name">maren</div>
      <div class="brand-sub">AESTHETICS</div>
    </div>
    <address class="contact" style="font-style: normal;">
      <div>4/27 Harbour Road</div>
      <div>Seacliff Bay</div>
      <div>Western Australia</div>
      <div class="phone">(08) 9555 0142</div>
      <div class="online">
        <div>www.marenaesthetics.com.au</div>
        <div>instagram maren_aesthetics</div>
        <div>facebook maren aesthetics australia</div>
      </div>
    </address>
  </aside>

  <h2 class="section-title ipl-title">IPL HAIR REMOVAL</h2>
  <ul class="price-list ipl">
    <li><span class="item">UPPER LIP</span><span>$50</span></li>
    <li><span class="item">CHIN</span><span>$50</span></li>
    <li><span class="item">CHEEKS</span><span>$75</span></li>
    <li><span class="item">WHOLE FACE</span><span>$350</span></li>
    <li class="gap"></li>
    <li><span class="item">BIKINI</span><span>$90</span></li>
    <li><span class="item">G STRING</span><span>$120</span></li>
    <li><span class="item">BRAZILIAN</span><span>$150</span></li>
    <li class="gap"></li>
    <li><span class="item">UNDERARMS</span><span>$90</span></li>
    <li><span class="item">HALF ARM</span><span>$180</span></li>
    <li><span class="item">FULL ARM</span><span>$250</span></li>
    <li><span class="item">HALF LEG</span><span>$290</span></li>
    <li><span class="item">THIGHS</span><span>$290</span></li>
    <li><span class="item">FULL LEG</span><span>$490</span></li>
    <li class="gap"></li>
    <li><span class="item">FULL BACK</span><span>$350</span></li>
    <li><span class="item">SHOULDERS</span><span>$180</span></li>
    <li><span class="item">NIPPLES</span><span>$60</span></li>
    <li><span class="item">SNAIL TRAIL</span><span>$50</span></li>
    <li><span class="item">STOMACH</span><span>$250</span></li>
    <li><span class="item">CHEST</span><span>$250</span></li>
    <li><span class="item">BUTTOCKS</span><span>$200</span></li>
  </ul>

  <h2 class="section-title photo-title">IPL PHOTO REJUVENATION</h2>
  <ul class="price-list photo">
    <li><span class="item">FULL FACE</span><span>$350</span></li>
    <li><span class="item">NECK</span><span>$200</span></li>
    <li><span class="item">FACE, NECK AND DÉCOLLETAGE</span><span>$450</span></li>
    <li><span class="item">SPOT TREATMENT</span><span>$50</span></li>
  </ul>

  <h2 class="section-title wax-title">WAXING</h2>
  <ul class="price-list wax">
    <li><span class="item">EYEBROW</span><span>$21</span></li>
    <li><span class="item">LIP</span><span>$15</span></li>
    <li><span class="item">CHIN</span><span>$15</span></li>
    <li><span class="item">SIDES OF FACE</span><span>$20</span></li>
    <li><span class="item">UNDERARM</span><span>$20</span></li>
    <li><span class="item">FOREARM</span><span>$25</span></li>
    <li><span class="item">FULL ARM</span><span>$35</span></li>
    <li><span class="item">LOWER LEG</span><span>$30</span></li>
    <li><span class="item">UPPER LEG</span><span>$30</span></li>
    <li><span class="item">FULL LEG</span><span>$50</span></li>
    <li><span class="item">INNER THIGH</span><span>$10</span></li>
    <li><span class="item">SNAIL TRAIL</span><span>$10</span></li>
    <li><span class="item">BIKINI</span><span>$30</span></li>
    <li><span class="item">G STRING</span><span>$40</span></li>
    <li><span class="item">BRAZILIAN</span><span>$50</span></li>
    <li class="gap"></li>
    <li><span class="item">EYEBROW WAX AND LIP WAX</span><span>$30</span></li>
    <li><span class="item">EYEBROW, LIP AND CHIN WAX</span><span>$45</span></li>
  </ul>

  <h2 class="section-title mens-title">MENS WAXING</h2>
  <ul class="price-list mens">
    <li><span class="item">MONO BROW</span><span>$5</span></li>
    <li><span class="item">EYEBROW</span><span>$21</span></li>
    <li><span class="item">NECK</span><span>$20</span></li>
    <li><span class="item">FULL BACK</span><span>$45</span></li>
    <li><span class="item">CHEST AND ABDOMEN</span><span>$45</span></li>
  </ul>
</main>
</body>
</html>
```